VORNAX Technologies Catalogue Design

We want the existing catalogue design to be completely re designed to have a better theme, that is professional and dynamic. we want the existing pictures changed, it would be great to have some images of local UAE population engaging in the activities shown. most of the written content remains the same. No.1 what we believe is to be removed. Point No. 3 all the little logos need to be re designed.

Target Market(s)

residential and corporate clients

Industry/Entity Type

home automation, command centers, audio video systems, lighting control systems

Requirements
Must have
• Point No. 3 all the little logos need to be re designed. Overall theme of the catalogue should look very good.
Nice to have
• Good font. Color theme can be related to logo which is black grey and red. Red maybe little less, leaving it to the designer to decide. it would be nice to have the cover of the catalogue clean and elegant. I have added doc of a pattern in blue color, it would be nice if it can be used as theme in the entire catalogue either in grey or black color, not blue.

```html
<!DOCTYPE html>
<html lang="en">
<head>
<meta charset="UTF-8">
<title>VORNAX Technologies — Company Profile 2022</title>
<link rel="stylesheet" href="https://fonts.googleapis.com/css2?family=Poppins:wght@500;600;700&display=swap">
<style>
  :root{
    --page-bg:#b4b4ad;
    --paper:#dedcd6;
    --red:#cc161c;
    --red-deep:#8e0f12;
    --slate:#6f7586;
    --ink:#262628;
    --white:#ffffff;
  }
  *{margin:0;padding:0;box-sizing:border-box}
  html,body{width:1200px;height:800px;overflow:hidden}
  body{background:var(--page-bg);font-family:'Poppins',sans-serif;position:relative}
  .cover{position:absolute;left:330px;top:20px;width:540px;height:760px;background:var(--paper);overflow:hidden;box-shadow:0 12px 30px rgba(0,0,0,.18)}
  .cover-shapes{position:absolute;inset:0}
  .brand{position:absolute;top:44px;right:40px;display:flex;align-items:center;gap:10px}
  .brand-dot{width:30px;height:30px;border-radius:50%;background:var(--red)}
  .brand-name{font-weight:700;font-size:26px;letter-spacing:5px;color:var(--ink);line-height:1}
  .brand-sub{display:block;font-weight:600;font-size:8.5px;letter-spacing:2.2px;color:var(--ink);margin-top:4px}
  .title{position:absolute;top:178px;right:56px;text-align:right;color:var(--white);font-weight:600;line-height:1.05}
  .title-line{display:block;font-size:28px;letter-spacing:1px}
  .title-year{display:block;font-size:50px;font-weight:700;margin-top:4px}
  .services{position:absolute;left:30px;top:496px;list-style:none;color:var(--white);font-weight:600;font-size:17px;line-height:1.5;letter-spacing:.4px}
  .offers{position:absolute;left:92px;top:640px;display:flex;gap:26px}
  .offer{width:72px;text-align:center}
  .offer-icon{display:block;width:72px;height:52px;border:1.5px solid var(--ink);background:var(--paper);padding:6px}
  .offer-icon span{display:block;width:100%;height:100%;background:linear-gradient(135deg,#3a3a3c,#8a8a8e)}
  .offer-icon.is-accent span{background:linear-gradient(135deg,var(--red),#3a3a3c)}
  .offer-label{display:block;margin-top:5px;font-size:7.5px;font-weight:600;color:var(--ink);line-height:1.2}
  .visit{position:absolute;right:30px;top:548px;color:var(--white);font-weight:700;font-size:26px;letter-spacing:1px}
  .web{position:absolute;right:0;top:606px;width:190px;height:26px;background:var(--red);color:var(--white);font-size:10.5px;font-weight:600;letter-spacing:2px;display:flex;align-items:center;justify-content:center}
</style>
</head>
<body>
  <article class="cover">
    <svg class="cover-shapes" viewBox="0 0 540 760" width="540" height="760" aria-hidden="false">
      <defs>
        <linearGradient id="cityTone" x1="0" y1="0" x2="1" y2="1">
          <stop offset="0" stop-color="#d21c20"/>
          <stop offset="1" stop-color="#6e0a0c"/>
        </linearGradient>
      </defs>
      <polygon class="red-field" points="175,150 540,150 540,430" fill="var(--red)"/>
      <g class="red-rules" stroke="#ffffff" stroke-width="1.4" opacity=".9">
        <line x1="440" y1="270" x2="540" y2="340"/>
        <line x1="420" y1="285" x2="540" y2="365"/>
        <line x1="405" y1="300" x2="540" y2="390"/>
        <line x1="390" y1="318" x2="510" y2="398"/>
      </g>
      <polygon role="img" aria-label="City skyline with a crowd of people, red duotone photograph" points="0,310 130,268 330,345 330,470 0,470" fill="url(#cityTone)"/>
      <polygon class="slate-band" points="110,240 540,400 540,450 110,292" fill="var(--slate)"/>
      <polygon class="slate-fold" points="110,240 130,268 110,292" fill="#3b3e46"/>
      <polygon class="ink-panel" points="0,470 345,470 375,372 392,605 0,605" fill="var(--ink)"/>
      <polygon class="visit-panel" points="290,575 540,520 540,632 360,632" fill="var(--ink)"/>
    </svg>

    <header class="brand">
      <span class="brand-dot"></span>
      <div>
        <span class="brand-name">VORNAX</span>
        <span class="brand-sub">TECHNOLOGIES L.L.C</span>
      </div>
    </header>

    <h1 class="title">
      <span class="title-line">COMPANY</span>
      <span class="title-line">PROFILE</span>
      <span class="title-year">2022</span>
    </h1>

    <ul class="services">
      <li>AUDIO VISUAL</li>
      <li>HOME AUTOMATION</li>
      <li>ELV SYSTEMS</li>
      <li>EMERING TECNOLOGIES</li>
    </ul>

    <div class="offers">
      <div class="offer">
        <span class="offer-icon is-accent"><span role="img" aria-label="Consultancy illustration"></span></span>
        <span class="offer-label">CONSULTANCY</span>
      </div>
      <div class="offer">
        <span class="offer-icon"><span role="img" aria-label="Project management illustration"></span></span>
        <span class="offer-label">PROJECT MANAGEMENT</span>
      </div>
      <div class="offer">
        <span class="offer-icon"><span role="img" aria-label="System integration illustration"></span></span>
        <span class="offer-label">SYSTEM INTEGRATION</span>
      </div>
      <div class="offer">
        <span class="offer-icon"><span role="img" aria-label="AMC service illustration"></span></span>
        <span class="offer-label">AMC SERVICE</span>
      </div>
    </div>

    <p class="visit">VISIT</p>
    <p class="web">www.vornaxtech.com</p>
  </article>
</body>
</html>
```